i need to make design for the our cover of three products:
Lemon scented Trash Bags
Strawberry scented Trash Bags
Lavender scented Trash Bags
all are with the same information i.e. the size, company name , number of bags etc the only difference is the scent
good examples are attached.
its also required that our brand is visible place in the design our brand "ovrolo" logo is attached as well
the cover design size is 10H*33W cm

Target Market(s)

commodity

Industry/Entity Type

plastic

Font styles to use
Serif
Sans Serif

```html
<!DOCTYPE html>
<html lang="en">
<head>
<meta charset="utf-8">
<title>ovrolo scented drawstring sacks – pack covers</title>
<link rel="stylesheet" href="https://fonts.googleapis.com/css2?family=Oswald:wght@400;500;600&family=Roboto+Condensed:wght@400;700&display=swap">
<style>
  :root {
    --green: #14925a;
    --green-dark: #0c7a48;
    --gold: #c9a27a;
    --gold-light: #ecd3b6;
    --top-band: #f0eef0;
    --ink-grey: #8a8a8a;
    --white: #ffffff;
  }
  * { box-sizing: border-box; margin: 0; padding: 0; }
  html, body { width: 1200px; height: 1200px; overflow: hidden; background: var(--white); }
  body { position: relative; font-family: "Oswald", sans-serif; }

  .cover {
    position: absolute;
    left: 157px;
    width: 885px;
    height: 268px;
    overflow: hidden;
    background: var(--tint);
  }
  .cover--lavender { top: 122px; --band: #c46cc1; --tint: #e7c2e4; --shield: #b75fb6; --photo-a: #b768c6; --photo-b: #8a59b8; }
  .cover--lemon { top: 469px; --band: #f6d000; --tint: #f2e8b4; --shield: #f4c800; --photo-a: #f8d700; --photo-b: #eab425; }
  .cover--strawberry { top: 817px; --band: #ee2e2c; --tint: #f8c8d0; --shield: #f02e2e; --photo-a: #f4413d; --photo-b: #d72a30; }

  .cover__top { position: absolute; left: 0; top: 0; width: 100%; height: 88px; background: var(--top-band); }
  .cover__band {
    position: absolute; left: 0; top: 88px; width: 100%; height: 92px;
    background: linear-gradient(180deg, var(--band) 0%, var(--band) 70%, color-mix(in srgb, var(--band) 85%, #000) 100%);
  }

  .product-title {
    position: absolute; left: 12px; top: 10px;
    font-family: "Oswald", sans-serif; font-weight: 600;
    font-size: 23px; letter-spacing: 0.2px; color: var(--green);
    transform: scaleX(0.92); transform-origin: left;
  }
  .product-specs {
    position: absolute; left: 12px; top: 42px;
    font-family: "Roboto Condensed", sans-serif; font-size: 8px;
    color: var(--ink-grey); letter-spacing: 0.3px;
  }

  .brand-name {
    position: absolute; left: 42px; top: 96px;
    font-family: "Oswald", sans-serif; font-weight: 400;
    font-size: 72px; line-height: 72px; color: var(--white);
    letter-spacing: 2px;
  }

  .scene-photo {
    position: absolute; inset: 0;
    clip-path: polygon(537px 0, 885px 0, 885px 268px, 319px 268px);
    background: radial-gradient(circle at 70% 40%, var(--photo-a) 0%, var(--photo-b) 100%);
  }

  .edge-line { position: absolute; inset: 0; pointer-events: none; }

  .scent-shield { position: absolute; left: 351px; top: 37px; width: 178px; height: 172px; }
  .scent-shield svg { position: absolute; inset: 0; }
  .scent-shield__text {
    position: absolute; left: 0; top: 30px; width: 100%;
    text-align: center; color: var(--white); font-family: "Oswald", sans-serif;
  }
  .scent-shield__name { font-size: 27px; line-height: 28px; font-weight: 500; }
  .scent-shield__name--long { font-size: 20px; line-height: 26px; }
  .scent-shield__kind { font-size: 27px; line-height: 28px; font-weight: 500; }
  .scent-shield__claim { font-size: 12px; line-height: 16px; letter-spacing: 0.5px; opacity: 0.9; }

  .count-banner {
    position: absolute; left: 353px; top: 220px; width: 532px; height: 33px;
    background: var(--green); border-top: 2px solid var(--white);
    clip-path: polygon(12px 0, 100% 0, 100% 100%, 0 100%);
    display: flex; align-items: center; justify-content: center;
    font-family: "Roboto Condensed", sans-serif; font-weight: 700;
    font-size: 21px; color: var(--white); letter-spacing: 0.4px;
  }

  .fit-note { position: absolute; left: 12px; top: 210px; display: flex; gap: 8px; align-items: flex-start; }
  .fit-note__can { width: 40px; height: 46px; }
  .fit-note__lines {
    font-family: "Roboto Condensed", sans-serif; font-size: 11.5px; line-height: 14.5px;
    color: var(--green); padding-top: 1px;
  }
  .fit-note__lines strong { font-weight: 700; color: var(--green-dark); }
</style>
</head>
<body>

<section class="cover cover--lavender" aria-label="Lavender scented pack cover">
  <div class="cover__top"></div>
  <div class="cover__band"></div>
  <div class="scene-photo" role="img" aria-label="Lavender flowers around a metal bin holding a tied drawstring bag"></div>
  <svg class="edge-line" viewBox="0 0 885 268"><line x1="540" y1="0" x2="320" y2="268" stroke="var(--gold)" stroke-width="4"/></svg>
  <h2 class="product-title">DRAWSTRING REFUSE SACKS</h2>
  <p class="product-specs">65x70 | LAVENDER SCENTED | PURPLE | 60 LT | 10 PCS</p>
  <div class="brand-name">ovrolo</div>
  <div class="scent-shield">
    <svg viewBox="0 0 178 172">
      <path d="M89 0 C120 10 150 12 178 10 L172 90 C165 130 130 155 89 172 C48 155 13 130 6 90 L0 10 C28 12 58 10 89 0 Z" fill="var(--gold)"/>
      <path d="M89 8 C117 17 144 19 168 18 L163 89 C156 124 126 146 89 162 C52 146 22 124 15 89 L10 18 C34 19 61 17 89 8 Z" fill="var(--gold-light)"/>
      <path d="M89 16 C114 24 138 26 159 26 L155 88 C148 119 122 138 89 152 C56 138 30 119 23 88 L19 26 C40 26 64 24 89 16 Z" fill="var(--shield)"/>
    </svg>
    <div class="scent-shield__text">
      <div class="scent-shield__name">LAVENDER</div>
      <div class="scent-shield__kind">SCENTED</div>
      <div class="scent-shield__claim">ODOR CONTROL</div>
    </div>
  </div>
  <div class="count-banner">10 MEDIUM PACKS | 15 GALLON DRAWSTRING</div>
  <div class="fit-note">
    <svg class="fit-note__can" viewBox="0 0 40 46">
      <path d="M3 4 H37 L33 44 H7 Z" fill="none" stroke="var(--green)" stroke-width="2"/>
      <text x="20" y="11" font-size="6" text-anchor="middle" fill="var(--green)" font-family="Roboto Condensed, sans-serif">FITS</text>
      <text x="20" y="27" font-size="16" font-weight="700" text-anchor="middle" fill="var(--green)" font-family="Roboto Condensed, sans-serif">15</text>
      <text x="20" y="35" font-size="5.5" text-anchor="middle" fill="var(--green)" font-family="Roboto Condensed, sans-serif">GALLON</text>
      <text x="20" y="41" font-size="5.5" text-anchor="middle" fill="var(--green)" font-family="Roboto Condensed, sans-serif">CAN</text>
    </svg>
    <p class="fit-note__lines">GRIPS-THE CAN<br><strong>TALL KITCHEN</strong><br>DRAWSTRING BAGS</p>
  </div>
</section>

<section class="cover cover--lemon" aria-label="Lemon scented pack cover">
  <div class="cover__top"></div>
  <div class="cover__band"></div>
  <div class="scene-photo" role="img" aria-label="Lemon slices and leaves around a metal bin holding a tied drawstring bag"></div>
  <svg class="edge-line" viewBox="0 0 885 268"><line x1="540" y1="0" x2="320" y2="268" stroke="var(--gold)" stroke-width="4"/></svg>
  <h2 class="product-title">DRAWSTRING REFUSE SACKS</h2>
  <p class="product-specs">65x70 | LEMON SCENTED | YELLOW | 60 LT | 10 PCS</p>
  <div class="brand-name">ovrolo</div>
  <div class="scent-shield">
    <svg viewBox="0 0 178 172">
      <path d="M89 0 C120 10 150 12 178 10 L172 90 C165 130 130 155 89 172 C48 155 13 130 6 90 L0 10 C28 12 58 10 89 0 Z" fill="var(--gold)"/>
      <path d="M89 8 C117 17 144 19 168 18 L163 89 C156 124 126 146 89 162 C52 146 22 124 15 89 L10 18 C34 19 61 17 89 8 Z" fill="var(--gold-light)"/>
      <path d="M89 16 C114 24 138 26 159 26 L155 88 C148 119 122 138 89 152 C56 138 30 119 23 88 L19 26 C40 26 64 24 89 16 Z" fill="var(--shield)"/>
    </svg>
    <div class="scent-shield__text">
      <div class="scent-shield__name">LEMON</div>
      <div class="scent-shield__kind">SCENTED</div>
      <div class="scent-shield__claim">ODOR CONTROL</div>
    </div>
  </div>
  <div class="count-banner">10 MEDIUM PACKS | 15 GALLON DRAWSTRING</div>
  <div class="fit-note">
    <svg class="fit-note__can" viewBox="0 0 40 46">
      <path d="M3 4 H37 L33 44 H7 Z" fill="none" stroke="var(--green)" stroke-width="2"/>
      <text x="20" y="11" font-size="6" text-anchor="middle" fill="var(--green)" font-family="Roboto Condensed, sans-serif">FITS</text>
      <text x="20" y="27" font-size="16" font-weight="700" text-anchor="middle" fill="var(--green)" font-family="Roboto Condensed, sans-serif">15</text>
      <text x="20" y="35" font-size="5.5" text-anchor="middle" fill="var(--green)" font-family="Roboto Condensed, sans-serif">GALLON</text>
      <text x="20" y="41" font-size="5.5" text-anchor="middle" fill="var(--green)" font-family="Roboto Condensed, sans-serif">CAN</text>
    </svg>
    <p class="fit-note__lines">GRIPS-THE CAN<br><strong>TALL KITCHEN</strong><br>DRAWSTRING BAGS</p>
  </div>
</section>

<section class="cover cover--strawberry" aria-label="Strawberry scented pack cover">
  <div class="cover__top"></div>
  <div class="cover__band"></div>
  <div class="scene-photo" role="img" aria-label="Strawberries around a metal bin holding a tied drawstring bag"></div>
  <svg class="edge-line" viewBox="0 0 885 268"><line x1="540" y1="0" x2="320" y2="268" stroke="var(--gold)" stroke-width="4"/></svg>
  <h2 class="product-title">DRAWSTRING REFUSE SACKS</h2>
  <p class="product-specs">65x70 | STRAWBERRY SCENTED | RED | 60 LT | 10 PCS</p>
  <div class="brand-name">ovrolo</div>
  <div class="scent-shield">
    <svg viewBox="0 0 178 172">
      <path d="M89 0 C120 10 150 12 178 10 L172 90 C165 130 130 155 89 172 C48 155 13 130 6 90 L0 10 C28 12 58 10 89 0 Z" fill="var(--gold)"/>
      <path d="M89 8 C117 17 144 19 168 18 L163 89 C156 124 126 146 89 162 C52 146 22 124 15 89 L10 18 C34 19 61 17 89 8 Z" fill="var(--gold-light)"/>
      <path d="M89 16 C114 24 138 26 159 26 L155 88 C148 119 122 138 89 152 C56 138 30 119 23 88 L19 26 C40 26 64 24 89 16 Z" fill="var(--shield)"/>
    </svg>
    <div class="scent-shield__text">
      <div class="scent-shield__name scent-shield__name--long">STRAWBERRY</div>
      <div class="scent-shield__kind">SCENTED</div>
      <div class="scent-shield__claim">ODOR CONTROL</div>
    </div>
  </div>
  <div class="count-banner">10 MEDIUM PACKS | 15 GALLON DRAWSTRING</div>
  <div class="fit-note">
    <svg class="fit-note__can" viewBox="0 0 40 46">
      <path d="M3 4 H37 L33 44 H7 Z" fill="none" stroke="var(--green)" stroke-width="2"/>
      <text x="20" y="11" font-size="6" text-anchor="middle" fill="var(--green)" font-family="Roboto Condensed, sans-serif">FITS</text>
      <text x="20" y="27" font-size="16" font-weight="700" text-anchor="middle" fill="var(--green)" font-family="Roboto Condensed, sans-serif">15</text>
      <text x="20" y="35" font-size="5.5" text-anchor="middle" fill="var(--green)" font-family="Roboto Condensed, sans-serif">GALLON</text>
      <text x="20" y="41" font-size="5.5" text-anchor="middle" fill="var(--green)" font-family="Roboto Condensed, sans-serif">CAN</text>
    </svg>
    <p class="fit-note__lines">GRIPS-THE CAN<br><strong>TALL KITCHEN</strong><br>DRAWSTRING BAGS</p>
  </div>
</section>

</body>
</html>
```